New Business Card Design Project

possibly double-sided card, with one side in color. leaves, a tree branch, or a tree of life, like laurel, olive, pine ... or a seed that grows. visual discreet and stylized or naive. no photo. no human silhouette Modern Typo possibly rounded corners matte paper, no selective varnish, neither gold nor silver English brief Double sided business card, with eventually a single colored side. Leaves, a tree branch or a tree of life, laurel, olive tree, pine tree ... or a growing seed. The design has to be discreet and stylized or naive. No human silhouettes Modern made Possibly rounded corners Matte paper, no selective varnish, no gold, no silver
Updates

I really prefer toned or subtles tones, Bluish / greenwich gray, verdigris ... Elegant and discreet colors Write "HUMANISTIC HYPNOTHERAPY, SYMBOLIC THERAPY" on 2 lines and on One side only (not with the name and address) Not use pictogram (such , address...)

Contact Information for Business Card

Hypnothérapie humaniste
Thérapie symbolique

Marianne Lebrodel
Hypnothérapeute
06 48 17 20 85
47 rue des Tilleuls-Brunoy, 33710 Morvalle
cabinet.lebrodel@velmoria.fr

Colors
33b8a4
3176b5

Requirements
Must have
• sober, elegant and refined card Sober design, elegant, plain
Nice to have
• desired colors: gray, blue-gis, greyish, khaki ... Desired colors: gray, blue-gray, grayish green, khaki, ...
Should not have
• gaudy colors, bright greens no bright gold neon colors

```html
<!DOCTYPE html>
<html lang="fr">
<head>
<meta charset="utf-8">
<title>Marianne Lebrodel – Carte de visite</title>
<link href="https://fonts.googleapis.com/css2?family=PT+Sans+Narrow:wght@400;700&display=swap" rel="stylesheet">
<style>
  :root {
    --page-bg: #eef1f1;
    --card-front: #dce3e2;
    --card-back: #ffffff;
    --ink-strong: #6a7573;
    --ink-soft: #8a9694;
    --leaf-grey: #c5cecc;
    --leaf-mint: #a9ecd3;
    --leaf-pale: #eef0f0;
  }
  * { margin: 0; padding: 0; box-sizing: border-box; }
  html, body {
    width: 1200px;
    height: 1000px;
    overflow: hidden;
    background: var(--page-bg);
    font-family: "PT Sans Narrow", "Arial Narrow", sans-serif;
  }
  .canvas {
    position: relative;
    width: 1200px;
    height: 1000px;
  }
  .card {
    position: absolute;
    left: 249px;
    width: 702px;
    height: 419px;
    border-radius: 36px;
    overflow: hidden;
  }
  .card--front {
    top: 53px;
    background: var(--card-front);
  }
  .card--back {
    top: 528px;
    background: var(--card-back);
    box-shadow: 0 0 0 1px #e3e8e8;
  }
  .foliage {
    position: absolute;
  }
  .card--front .foliage--top-left {
    left: -20px;
    top: -20px;
    width: 310px;
    height: 260px;
    background: radial-gradient(ellipse at 35% 40%, var(--leaf-grey) 0%, rgba(197,206,204,0.5) 40%, rgba(220,227,226,0) 72%);
  }
  .card--front .foliage--bottom-right {
    left: 250px;
    top: 180px;
    width: 470px;
    height: 260px;
    background: radial-gradient(ellipse at 60% 70%, var(--leaf-grey) 0%, rgba(197,206,204,0.5) 40%, rgba(220,227,226,0) 72%);
  }
  .card--back .foliage--right {
    left: 465px;
    top: 20px;
    width: 245px;
    height: 400px;
    background:
      radial-gradient(ellipse at 50% 72%, var(--leaf-mint) 0%, rgba(169,236,211,0.45) 35%, rgba(255,255,255,0) 62%),
      radial-gradient(ellipse at 65% 28%, var(--leaf-pale) 0%, rgba(238,240,240,0.6) 40%, rgba(255,255,255,0) 70%);
  }
  .tagline {
    position: absolute;
    left: 0;
    right: 0;
    top: 180px;
    text-align: center;
    color: var(--ink-strong);
    padding-left: 0;
  }
  .tagline__main {
    font-weight: 700;
    font-size: 31px;
    line-height: 1;
    letter-spacing: 0.2px;
  }
  .tagline__sub {
    font-weight: 400;
    font-size: 24px;
    line-height: 1.1;
    margin-top: 0;
  }
  .identity {
    position: absolute;
    left: 49px;
    top: 118px;
  }
  .identity__name {
    font-weight: 700;
    font-size: 30px;
    line-height: 1;
    color: var(--ink-strong);
    text-transform: uppercase;
  }
  .identity__role {
    font-size: 24px;
    line-height: 1.2;
    color: var(--ink-soft);
  }
  .contact {
    position: absolute;
    left: 49px;
    top: 249px;
    list-style: none;
    color: var(--ink-strong);
    font-size: 17px;
  }
  .contact li {
    height: 29px;
    line-height: 24px;
  }
  .contact__phone { font-weight: 700; }
</style>
</head>
<body>
<div class="canvas">
  <section class="card card--front">
    <div class="foliage foliage--top-left" role="img" aria-label="Branche d'olivier stylisée en ton gris discret"></div>
    <div class="foliage foliage--bottom-right" role="img" aria-label="Branche d'olivier stylisée avec olives, en gris discret"></div>
    <div class="tagline">
      <p class="tagline__main">HYPNOTHÉRAPIE HUMANISTE</p>
      <p class="tagline__sub">Thérapie symbolique</p>
    </div>
  </section>

  <section class="card card--back">
    <div class="foliage foliage--right" role="img" aria-label="Branches d'olivier stylisées, feuilles vert d'eau et gris pâle"></div>
    <div class="identity">
      <h1 class="identity__name">Marianne Lebrodel</h1>
      <p class="identity__role">Hypnothérapeute</p>
    </div>
    <ul class="contact">
      <li class="contact__phone">06 48 17 20 85</li>
      <li class="contact__address">47 rue des Tilleuls-Brunoy, 33710 Morvalle</li>
      <li class="contact__email">cabinet.lebrodel@velmoria.fr</li>
    </ul>
  </section>
</div>
</body>
</html>
```